Brasko Construction Business Card

I need a business card design for my company.
We are a construction/machinery company.
I would like to see my logo on the front of the card and my details on the other side
I would like the card to be black or dark grey in colour,with my logo as i send it or modified with a lighter blue colour
I would like to see the design kept fairly simple,but eye catching at the same time
Industry/Entity Type
Business
Contact Information for Business Card
Name
Phone Number
Address
Email
Colors
00a990
1b1b1b
000000
474747
ececec

```html
<!DOCTYPE html>
<html lang="en">
<head>
<meta charset="UTF-8">
<title>Brasko Construction Business Card</title>
<link href="https://fonts.googleapis.com/css2?family=Open+Sans:wght@400;600;700&display=swap" rel="stylesheet">
<style>
  :root {
    --teal: #00a990;
    --ink: #1b1b1b;
    --black: #000000;
    --grey: #474747;
    --paper: #ececec;
    --white: #ffffff;
    --stage: #d9d6d0;
  }
  * { box-sizing: border-box; margin: 0; padding: 0; }
  html, body { width: 1200px; height: 1062px; overflow: hidden; }
  body {
    background: var(--stage);
    font-family: "Open Sans", Arial, sans-serif;
    position: relative;
  }
  .card {
    position: absolute;
    left: 250px;
    width: 700px;
    height: 400px;
    overflow: hidden;
    box-shadow: 0 10px 30px rgba(0,0,0,.25);
  }
  .card--front { top: 90px; background: linear-gradient(160deg, var(--white) 0%, var(--paper) 100%); }
  .card--back { top: 572px; background: linear-gradient(150deg, var(--grey) 0%, var(--ink) 45%, var(--black) 100%); }
  .card__curve { position: absolute; inset: 0; width: 100%; height: 100%; }

  .brand { position: absolute; display: flex; align-items: center; gap: 12px; }
  .brand__mark { width: 18px; height: 18px; border-radius: 50%; background: var(--teal); flex: none; }
  .brand__name { font-weight: 700; text-transform: uppercase; letter-spacing: 2px; line-height: 1.1; white-space: nowrap; }
  .brand__line { display: block; }

  .card--front .brand { left: 70px; top: 70px; }
  .card--front .brand__name { font-size: 28px; color: var(--ink); }

  .contact { position: absolute; left: 440px; top: 58px; list-style: none; }
  .contact__item { display: flex; align-items: center; gap: 10px; font-size: 15px; color: var(--grey); margin-bottom: 12px; white-space: nowrap; }
  .contact__icon { width: 14px; height: 14px; flex: none; }

  .holder { position: absolute; left: 70px; top: 250px; }
  .holder__name { font-size: 24px; font-weight: 600; color: var(--grey); }
  .holder__role { font-size: 17px; color: #9a9a9a; }

  .card--back .brand { left: 50%; top: 50%; transform: translate(-50%, -50%); }
  .card--back .brand__name { font-size: 40px; color: var(--white); }
</style>
</head>
<body>

<section class="card card--front" aria-label="Card front">
  <svg class="card__curve" viewBox="0 0 700 400" preserveAspectRatio="none" aria-hidden="true">
    <path d="M430 400 C 560 330, 650 250, 700 150 L700 400 Z" fill="var(--teal)"/>
    <path d="M452 400 C 575 340, 660 262, 700 178 L700 400 Z" fill="var(--white)"/>
    <path d="M462 400 C 585 345, 665 270, 700 190 L700 400 Z" fill="var(--black)"/>
  </svg>

  <div class="brand">
    <span class="brand__mark"></span>
    <span class="brand__name"><span class="brand__line">Brasko</span><span class="brand__line">Construction</span></span>
  </div>

  <ul class="contact">
    <li class="contact__item">
      <svg class="contact__icon" viewBox="0 0 16 16" aria-hidden="true"><path d="M4 1l2.5 3-1.5 1.5c1 2 2.5 3.5 4.5 4.5L11 8.5l3 2.5-1.5 3C7 13.5 2.5 9 2 3.5z" fill="var(--grey)"/></svg>
      555 014 2287
    </li>
    <li class="contact__item">
      <svg class="contact__icon" viewBox="0 0 16 16" aria-hidden="true"><circle cx="8" cy="8" r="6.5" fill="none" stroke="var(--grey)" stroke-width="1.3"/><path d="M1.5 8h13M8 1.5c-3 3.5-3 9.5 0 13M8 1.5c3 3.5 3 9.5 0 13" fill="none" stroke="var(--grey)" stroke-width="1.1"/></svg>
      www.danawhitlow.com
    </li>
    <li class="contact__item">
      <svg class="contact__icon" viewBox="0 0 16 16" aria-hidden="true"><text x="8" y="13" text-anchor="middle" font-size="15" font-weight="700" fill="var(--ink)" font-family="Open Sans, sans-serif">@</text></svg>
      dana@whitlowmail.com
    </li>
  </ul>

  <div class="holder">
    <p class="holder__name">Dana Whitlow</p>
    <p class="holder__role">Manager</p>
  </div>
</section>

<section class="card card--back" aria-label="Card back">
  <div class="brand">
    <span class="brand__mark"></span>
    <span class="brand__name"><span class="brand__line">Brasko</span><span class="brand__line">Construction</span></span>
  </div>
</section>

</body>
</html>
```